Outsourced Accounting Services - images Brightpane Ad Circuits (BAC) ads needed

I am looking for graphic designer who has experienced in creating images for Brightpane Ad Circuits (BAC) ads.

IMPORTANT NOTES:
Designer has to provide total 27 image dimensions and also the editable artwork file in AI format.

The design created has to be professional and be able to grab attention visually. The message on the ad also has to be clear.

OVERVIEW:
Client is in the business of providing corporate services in Singapore.
They are targeting businesses to take up their Outsourced Accounting Services.
You may find out more info for this service at https://www.ledgerharbourhub.example/outsourced-accounting-services/

Kindly find below the information of the image dimension required, file formats and file size.

==========================================
File Formats: GIF, JPG, PNG
Max. size :150KB

Ad sizes:
200 × 200 Small square
240 × 400 Vertical rectangle
250 × 250 Square
250 × 360 Triple widescreen
300 × 250 Inline rectangle
336 × 280 Large rectangle
580 × 400 Netboard
120 × 600 Skyscraper
160 × 600 Wide skyscraper
300 × 600 Half-page ad
300 × 1050 Portrait
468 × 60 Banner
728 × 90 Leaderboard
930 × 180 Top banner
970 × 90 Large leaderboard
970 × 250 Billboard
980 × 120 Panorama

Target Market(s)

The objective of the ad is to attract the attention of business owners or key decision makers who are looking to enjoy cost savings + achieve professional accounting function through Outsourced Accounting Services (instead of having a in-house accounting team).

Industry/Entity Type

Accounting

Font styles to use
Sans Serif
Other font styles liked:
• roboto

Colors

Designer to choose colors to be used in the design.

Requirements
Must have
• Well thought-out and crafted design to communicate ideas to targeted audience.
Should not have
• 1) No cartoon or cute or funny designs.
• 2) No funny text
• 3) No red / pink / purple colour

```html
<!DOCTYPE html>
<html lang="en">
<head>
<meta charset="UTF-8">
<title>Corvane Advisory – Outsourced Accounting Display Ads</title>
<link href="https://fonts.googleapis.com/css2?family=Roboto:wght@500;700&display=swap" rel="stylesheet">
<style>
  :root {
    --blue-light: #00b6d9;
    --blue-deep: #0a78bd;
    --orange: #ff6d00;
    --white: #ffffff;
    --navy: #1c4a8c;
    --cream-light: #f6f2dc;
    --cream-warm: #e7dcb8;
    --frame: #1a1a1a;
  }
  * { box-sizing: border-box; margin: 0; padding: 0; }
  html, body { width: 1200px; height: 800px; overflow: hidden; background: var(--white); }
  body { position: relative; font-family: "Roboto", Arial, sans-serif; color: var(--white); }

  .ad { position: absolute; overflow: hidden; border: 1px solid var(--frame); background: var(--white); }
  .ad-skyscraper { left: 135px; top: 100px; width: 160px; height: 600px; }
  .ad-leaderboard { left: 338px; top: 100px; width: 728px; height: 90px; }
  .ad-rectangle { left: 351px; top: 420px; width: 336px; height: 280px; }

  .photo {
    position: absolute;
    background: linear-gradient(160deg, var(--cream-light) 0%, var(--cream-warm) 100%);
  }
  .shapes { position: absolute; left: 0; top: 0; }
  .content { position: absolute; }

  .headline { font-weight: 700; text-transform: uppercase; letter-spacing: 0.2px; }
  .divider { position: absolute; background: rgba(255,255,255,0.75); }
  .subline { font-weight: 500; }
  .cta {
    position: absolute; background: var(--orange); color: var(--white);
    font-weight: 700; text-transform: uppercase; display: flex;
    align-items: center; justify-content: center;
  }
  .brand {
    position: absolute; display: flex; flex-direction: column; align-items: center;
    color: var(--navy); font-family: "Roboto", Arial, sans-serif; font-weight: 700;
    text-transform: uppercase; line-height: 1.05; text-align: center;
  }
  .brand-mark { background: var(--navy); margin-bottom: 4px; }

  /* Skyscraper 160 x 600 */
  .ad-skyscraper .photo { left: 0; top: 330px; width: 160px; height: 270px; }
  .ad-skyscraper .headline { position: absolute; left: 10px; top: 30px; width: 150px; font-size: 14px; line-height: 18px; }
  .ad-skyscraper .divider { left: 6px; top: 125px; width: 142px; height: 1px; }
  .ad-skyscraper .subline { position: absolute; left: 7px; top: 134px; width: 150px; font-size: 13px; line-height: 17px; }
  .ad-skyscraper .cta { left: 8px; top: 218px; width: 115px; height: 33px; font-size: 16px; }
  .ad-skyscraper .brand { left: 62px; top: 278px; width: 96px; font-size: 11px; }
  .ad-skyscraper .brand-mark { width: 22px; height: 22px; }

  /* Leaderboard 728 x 90 */
  .ad-leaderboard .photo { left: 560px; top: 0; width: 168px; height: 90px; }
  .ad-leaderboard .headline { position: absolute; left: 0; top: 16px; width: 268px; font-size: 16px; line-height: 21px; text-align: center; }
  .ad-leaderboard .divider { left: 267px; top: 14px; width: 1px; height: 64px; }
  .ad-leaderboard .subline { position: absolute; left: 272px; top: 14px; width: 142px; font-size: 13px; line-height: 16px; text-align: center; }
  .ad-leaderboard .cta { left: 417px; top: 36px; width: 116px; height: 33px; font-size: 16px; }
  .ad-leaderboard .brand { left: 538px; top: 5px; width: 70px; font-size: 9px; }
  .ad-leaderboard .brand-mark { width: 16px; height: 16px; margin-bottom: 3px; }

  /* Rectangle 336 x 280 */
  .ad-rectangle .photo { left: 0; top: 0; width: 336px; height: 280px; }
  .ad-rectangle .headline { position: absolute; left: 11px; top: 6px; width: 200px; font-size: 18px; line-height: 23px; }
  .ad-rectangle .divider { left: 6px; top: 121px; width: 144px; height: 1px; }
  .ad-rectangle .subline { position: absolute; left: 6px; top: 124px; width: 160px; font-size: 14px; line-height: 17px; }
  .ad-rectangle .cta { left: 26px; top: 231px; width: 139px; height: 38px; font-size: 19px; }
  .ad-rectangle .brand { left: 244px; top: 12px; width: 92px; font-size: 11px; }
  .ad-rectangle .brand-mark { width: 24px; height: 24px; }
</style>
</head>
<body>

<!-- Wide skyscraper -->
<section class="ad ad-skyscraper">
  <div class="photo" role="img" aria-label="Photo of a young professional in glasses writing at a desk"></div>
  <svg class="shapes" width="160" height="600" viewBox="0 0 160 600" aria-hidden="true">
    <defs>
      <linearGradient id="sky-blue" x1="0" y1="0" x2="0" y2="1">
        <stop offset="0" stop-color="#00b6d9"/>
        <stop offset="1" stop-color="#0a78bd"/>
      </linearGradient>
    </defs>
    <polygon points="160,222 160,360 25,360" fill="#ffffff"/>
    <polygon points="0,0 160,0 160,222 25,342 0,342" fill="url(#sky-blue)"/>
  </svg>
  <div class="content">
    <h2 class="headline">Save up to 79% on salaries with outsourced accounting services</h2>
    <span class="divider"></span>
    <p class="subline">More Savings on training office space and administrative overhead</p>
    <a class="cta">Learn more</a>
    <div class="brand"><span class="brand-mark"></span>Corvane<br>Advisory</div>
  </div>
</section>

<!-- Leaderboard -->
<section class="ad ad-leaderboard">
  <div class="photo" role="img" aria-label="Photo of a young professional in glasses writing at a desk"></div>
  <svg class="shapes" width="728" height="90" viewBox="0 0 728 90" aria-hidden="true">
    <defs>
      <linearGradient id="lead-blue" x1="0" y1="0" x2="1" y2="0">
        <stop offset="0" stop-color="#0a8ac6"/>
        <stop offset="1" stop-color="#0a9fd3"/>
      </linearGradient>
    </defs>
    <polygon points="502,0 625,0 580,90 597,90" fill="#ffffff"/>
    <polygon points="0,0 502,0 597,90 0,90" fill="url(#lead-blue)"/>
  </svg>
  <div class="content">
    <h2 class="headline">Save up to 79% on<br>salaries with outsourced<br>accounting services</h2>
    <span class="divider"></span>
    <p class="subline">More Savings on training office space and administrative overhead</p>
    <a class="cta">Learn more</a>
    <div class="brand"><span class="brand-mark"></span>Corvane<br>Advisory</div>
  </div>
</section>

<!-- Large rectangle -->
<section class="ad ad-rectangle">
  <div class="photo" role="img" aria-label="Photo of a young professional in glasses writing at a desk"></div>
  <svg class="shapes" width="336" height="280" viewBox="0 0 336 280" aria-hidden="true">
    <defs>
      <linearGradient id="rect-blue" x1="0" y1="0" x2="0.4" y2="1">
        <stop offset="0" stop-color="#00b6d9"/>
        <stop offset="1" stop-color="#0a78bd"/>
      </linearGradient>
    </defs>
    <polygon points="277,0 336,0 336,112 210,80" fill="#ffffff"/>
    <polygon points="0,0 277,0 97,220 0,220" fill="url(#rect-blue)"/>
  </svg>
  <div class="content">
    <h2 class="headline">Save up to 79%<br>on salaries<br>with outsourced<br>accounting<br>services</h2>
    <span class="divider"></span>
    <p class="subline">More Savings on<br>training office space<br>and administrative<br>overhead</p>
    <a class="cta">Learn more</a>
    <div class="brand"><span class="brand-mark"></span>Corvane<br>Advisory</div>
  </div>
</section>

</body>
</html>
```